KRV Anti-Money Laundering Postcard

We are a U.S. based regulatory compliance consulting company who services the financial industry (stock, bonds, equities, banking, etc.)

One of the services that we offer is Independent Anti-Money Laundering audit reviews. These reviews are required by U.S. law for certain financial institutions.

We are looking for a 6" x 8.5" horizontally oriented postcard to market our services in this business. The card should be sharp and professional.

The font and back of the card must have our logo and include

"Anti-Money Laundering Compliance" or "Anti-Money Laundering Compliance Services"

We would like the following message to be included on the card either on the front or preferably the back:

"Belwick & Associates are specialists in Anti-Money Laundering compliance. Our firm’s Anti-Money Laundering compliance solutions include:

• Independent Money Laundering Audits
• Anti-Money Laundering Compliance Procedures
• Anti-Money Laundering Training

Let our expert compliance team assist you in ensuring that your firm is compliant with all of its money laundering and other compliance obligations.

The back of the card should have our address, website, phone number and website: The address is normally included in the return address section noted in the Post Office requirements section blow.

42 W. Calloway Street, Suite 300
Fairhaven, CA 90217
(877) 318-4092
info@belwickandassociates.example
www.belwickandassociates.example

Back of the postcard Post Office Design requirements:

http://www.quillmailprint.example/products/postcard-deluxe

Target Market(s)

Stock Brokerage Firms, Investment Advisers, Banks and other financial institutions

Industry/Entity Type

Financial Planning

Font styles to use
Sans Serif

Requirements
Must have
• Our Logo on the front and back. Clean and professional. Nice artwork.

```html
<!DOCTYPE html>
<html lang="en">
<head>
<meta charset="utf-8">
<title>Belwick &amp; Associates – Anti-Money Laundering Postcard</title>
<link rel="stylesheet" href="https://fonts.googleapis.com/css2?family=Lato:wght@300;400&family=Ubuntu:wght@400;500&display=swap">
<style>
  :root {
    --backdrop: #c8d3b9;
    --charcoal: #30343a;
    --ribbon: #9b1b1f;
    --ribbon-fold: #5e1013;
    --paper: #ffffff;
    --paper-grey: #e2e2e2;
    --ink: #1d1d1d;
    --light-ink: #f2f2f2;
  }
  * { margin: 0; padding: 0; box-sizing: border-box; }
  html, body { width: 1200px; height: 1200px; overflow: hidden; }
  body { background: var(--backdrop); position: relative; font-family: "Lato", sans-serif; }

  .postcard { position: absolute; top: 407px; width: 548px; height: 354px; overflow: visible; }
  .postcard--front { left: 46px; background: var(--charcoal); }
  .postcard--back { left: 613px; background: var(--paper-grey); }

  /* ribbons */
  .ribbon {
    position: absolute; left: 0; height: 25px; background: var(--ribbon);
    color: var(--light-ink); display: flex; align-items: center; z-index: 2;
  }
  .ribbon::after {
    content: ""; position: absolute; right: 0; bottom: -6px;
    border-top: 6px solid var(--ribbon-fold); border-left: 6px solid transparent;
  }

  /* front */
  .front-intro, .front-closing {
    position: absolute; left: 28px; width: 330px;
    color: var(--light-ink); font-weight: 300; font-size: 13px; line-height: 16px;
  }
  .front-intro { top: 62px; }
  .front-closing { top: 284px; left: 29px; }
  .service { width: 385px; padding-left: 28px; font-family: "Ubuntu", sans-serif; font-size: 14px; letter-spacing: 0.3px; }
  .service--audits { top: 122px; }
  .service--procedures { top: 165px; }
  .service--training { top: 208px; padding-left: 29px; }

  .front-panel { position: absolute; left: 378px; top: 0; width: 170px; height: 354px; background: var(--paper); z-index: 1; }
  .brand {
    display: flex; align-items: center; justify-content: center; gap: 6px;
    font-family: "Ubuntu", sans-serif; font-weight: 500; color: var(--ink);
  }
  .brand__mark { width: 12px; height: 12px; background: var(--ribbon); flex: none; }
  .front-panel .brand { position: absolute; top: 52px; left: 0; width: 170px; font-size: 15px; }
  .tagline {
    position: absolute; top: 166px; left: 0; width: 170px; text-align: center;
    font-family: "Ubuntu", sans-serif; font-size: 17px; line-height: 28px; color: var(--ink);
  }

  /* back */
  .contact-block { position: absolute; left: 0; top: 0; width: 238px; height: 189px; background: var(--charcoal); }
  .contact { width: 246px; justify-content: flex-end; padding-right: 19px; font-size: 11px; }
  .contact--street { top: 15px; }
  .contact--city { top: 50px; }
  .contact--phone { top: 85px; }
  .contact--email { top: 119px; }
  .contact--web { top: 154px; }
  .postcard--back .brand { position: absolute; top: 255px; left: 0; width: 246px; font-size: 20px; }
</style>
</head>
<body>
  <section class="postcard postcard--front" aria-label="Postcard front">
    <p class="front-intro">Belwick &amp; Associates are specialists in Anti-Money Laundering compliance. Our firm’s Anti-Money Laundering compliance solutions include:</p>
    <div class="ribbon service service--audits">Independent Money Laundering Audits</div>
    <div class="ribbon service service--procedures">Anti-Money Laundering Compliance Procedures</div>
    <div class="ribbon service service--training">Anti-Money Laundering Training</div>
    <p class="front-closing">Let our expert compliance team assist you in ensuring that your firm is compliant with all of its money laundering and other compliance obligations</p>
    <div class="front-panel">
      <div class="brand"><span class="brand__mark"></span><span>Belwick &amp; Associates</span></div>
      <p class="tagline">Anti-Money<br>Laundering<br>Compliance<br>Services</p>
    </div>
  </section>

  <section class="postcard postcard--back" aria-label="Postcard back">
    <div class="contact-block"></div>
    <div class="ribbon contact contact--street">42 W. Calloway Street, Suite 300</div>
    <div class="ribbon contact contact--city">Fairhaven, CA 90217</div>
    <div class="ribbon contact contact--phone">(877) 318-4092</div>
    <div class="ribbon contact contact--email">info@belwickandassociates.example</div>
    <div class="ribbon contact contact--web">www.belwickandassociates.example</div>
    <div class="brand"><span class="brand__mark"></span><span>Belwick &amp; Associates</span></div>
  </section>
</body>
</html>
```